WORDPRESS DESIGN - PROFESSIONAL SERVICES

Objective:
Design a new Wordpress e-commerce website for www.brolvanecareers.com.au .

BRLV Careers provides professional CV/resume writing services for Australian IT professionals. This assignment is to upgrade an existing 25 page e-commerce website - www.brolvanecareers.com.au

Process:
The contract is to design of the website. PixelForum designers need to submit a home page design based on the attached files and wireframes. BRLV will judge these submissions and the winner will be awarded $350 to design the 25 page website for Wordpress

Design:
You will be given Quartzly Wireframes, images and copy to base your design on. You can choose any font or colour palette, although it is preferred if you base it on the existing logo.

The design must be:
• Corporate
• Compelling
• Trustworthy

Development:
Development will be a separate assignment. The existing website to be upgraded is built on WordPress and Tradeloom.

You will be provided:
a) Logo
b) Suggested Colour palette
c) 25 Quartzly Wireframes
d) Images
e) Copy

Process:
1) Submit home page designs based on Home ATF and Home BTF.
2) Winner gets $350 design contract
3) Design sign-off
4) Payment

Target Market(s)

Customer Profile:

• Professional
• IT Professionals
• Earn $100k+
• Corporate
• University/Tertiary Educatation
• 80% men
• Live in Australian cities
• Mix of European, Indian and Asian backgrounds
• 75% are 30-50 y/o

Industry/Entity Type

E-Commerce

Font styles to use
Sans Serif

Colors
0355a3
3176b5
85abd2

Requirements
Must have
• The design must be:
• Corporate
• Compelling
• Trustworthy

* Lay-out should be based on the wireframes provided by BRLV
* The top banner is very important and will be on every page.
* There are a lot of words on the page so one of the challenges is to make it not look crowded and busy.
* It needs to look modern and professional. Use some creativity.
* The three key buttons we want users to click is the 'Click Me' next to products and the 'Shop' icon. Please highlight these (maybe in a different colour or with a frame)
* The font is very important.
Nice to have
• The font and colour palette you choose matches the existing logo

```html
<!DOCTYPE html>
<html lang="en">
<head>
<meta charset="utf-8">
<title>BRLV Careers – CV Writing for IT Professionals</title>
<link rel="stylesheet" href="https://fonts.googleapis.com/css2?family=Open+Sans:wght@400;600&family=Bitter:wght@700&display=swap">
<style>
:root{
  --brand:#0563ae;
  --brand-dark:#04508f;
  --brand-mid:#3176b5;
  --brand-light:#85abd2;
  --navy:#0d2c57;
  --text:#555;
  --muted:#8a8a8a;
  --line:#e6e6e6;
  --panel:#f7f7f7;
  --seal:#2b9bd8;
  --gold:#f0a81c;
}
*{box-sizing:border-box;margin:0;padding:0}
html,body{width:1200px;height:1147px;overflow:hidden;background:#fff}
body{font-family:"Open Sans",sans-serif;color:var(--text)}
.page{position:absolute;left:0;top:0;width:1400px;height:1338px;transform:scale(.857143);transform-origin:0 0}
.abs{position:absolute}

.main-nav{left:201px;top:34px;width:1000px;height:64px;background:var(--brand);display:flex;align-items:center}
.main-nav a{color:#fff;text-decoration:none;font-size:15px;height:64px;line-height:64px;text-align:center;border-right:1px solid var(--brand-dark);white-space:nowrap;flex:none}
.main-nav .cart{flex:1;border:0;font-size:24px;text-align:right;padding-right:17px}

.banner{left:201px;top:98px;width:1000px;height:136px;background:linear-gradient(100deg,#f4f9fd 0%,#dfeef8 35%,#bcdcef 55%,#eaf4fb 70%,#9fcbe6 85%,#d8ecf7 100%);overflow:hidden}
.brand-dot{left:24px;top:53px;width:30px;height:30px;border-radius:50%;background:var(--brand)}
.brand-name{left:64px;top:54px;font-size:19px;font-weight:600;color:var(--navy);white-space:nowrap}
.banner h1{left:215px;top:42px;font-family:"Bitter",serif;font-size:37px;color:var(--navy);white-space:nowrap}

.product{width:329px;height:408px;top:263px;border:1px solid var(--line);background:#fff}
.product-head{height:73px;background:var(--brand);color:#fff;font-size:16.5px;line-height:28px;padding:9px 19px}
.product-photo{left:15px;top:96px;width:106px;height:112px;border:1px solid #ddd;padding:3px;background:#fff}
.product-photo div{width:100%;height:100%}
.price{left:142px;top:95px;font-size:13px;line-height:22px}
.btn-click{left:141px;top:142px;width:88px;height:26px;background:linear-gradient(#2d8fd6,#0563ae);color:#fff;font-size:10.5px;text-align:center;line-height:26px;border-radius:2px}
.stars{left:250px;top:146px;font-size:14px;letter-spacing:-1px;color:var(--gold)}
.stars span{color:#ccc}
.reviews{left:145px;top:173px;font-size:13px;color:var(--muted);line-height:20px}
.features{left:0;top:225px;width:327px;list-style:none}
.features li{height:35px;line-height:35px;border-bottom:1px solid var(--line);font-size:13px;color:var(--muted);padding-left:52px;position:relative;white-space:nowrap}
.features li:last-child{border:0}
.features svg{position:absolute;left:20px;top:10px}

.side-card{left:903px;top:263px;width:298px;height:403px;border:1px solid var(--line)}
.side-row{left:0;width:296px;border-bottom:1px solid var(--line)}
.seal{border-radius:50%;background:var(--seal)}
.track{left:135px;top:100px;font-size:13px;line-height:24.7px;color:#222;white-space:nowrap}
.track .dim{color:var(--text)}
.partner{top:253px;height:34px;border-radius:3px;background:#e3e8ee}
.contact-photo{left:15px;top:306px;width:82px;height:96px;background:linear-gradient(#c7cdd6,#2a3140)}
.contact-text{left:113px;top:334px;font-size:14px;line-height:22px;white-space:nowrap}

.social{left:903px;width:298px;height:49px;color:#fff;font-size:15px;padding-left:20px;line-height:49px;border-radius:2px}
.social .ico{position:absolute;right:20px;top:9px;width:30px;height:30px;border-radius:3px;background:rgba(255,255,255,.9)}
.social.linkfolio{top:686px;background:linear-gradient(#1a6cb4,#04508f)}
.social.circlepost{top:743px;background:linear-gradient(#e2473c,#c52820)}

.testi-card{left:903px;top:813px;width:298px;height:249px;border:1px solid var(--line)}
.testi-head{height:49px;background:var(--brand);color:#fff;font-size:20px;line-height:54px;padding-left:14px}
.testi-photo{left:100px;top:63px;width:98px;height:98px;border-radius:50%;background:radial-gradient(circle at 50% 40%,#d9dde3,#7b8694)}
.testi-text{left:14px;top:170px;width:268px;text-align:center;font-size:13px;line-height:22px;color:var(--muted)}

.register{left:904px;top:1078px;width:297px;height:111px;background:var(--brand);color:#fff;text-align:center;padding-top:12px}
.register strong{font-weight:400;font-size:20.5px;display:block;line-height:32px}
.register span{font-size:16px;line-height:28px}

.shop-band{left:201px;top:686px;width:673px;height:50px;background:var(--brand);color:#fff;font-size:14px;line-height:50px;padding-left:22px;white-space:nowrap}
.how{left:201px;top:736px;width:673px;height:275px;background:var(--panel)}
.how h2{left:24px;top:18px;font-weight:400;font-size:19px;color:var(--brand-mid);white-space:nowrap}
.how ol{left:25px;top:57px;font-size:14.5px;line-height:32px;list-style:none;counter-reset:n;white-space:nowrap}
.how li{counter-increment:n}
.how li::before{content:counter(n) ". ";color:var(--muted)}

.section-title{left:201px;top:1024px;font-size:20px;color:#222;font-weight:400}
.quote{left:201px;top:1066px;width:673px;height:124px;border:1px solid var(--line);background:var(--panel)}
.quote-photo{left:18px;top:10px;width:107px;height:107px;border-radius:50%;background:radial-gradient(circle at 45% 40%,#f0c6a2,#a2663b)}
.quote h3{left:160px;top:18px;font-size:15px;font-weight:600;color:#666}
.quote p{left:158px;top:46px;width:470px;font-size:13px;line-height:22px;color:var(--muted)}

.site-footer{left:200px;top:1222px;width:1001px;height:78px;background:var(--brand);color:#fff;font-size:12.5px;line-height:80px}
.site-footer .copy{left:21px}
.site-footer nav{right:18px;top:0}
</style>
</head>
<body>
<div class="page">

  <nav class="main-nav abs">
    <a style="width:109px">Home</a><a style="width:99px">Shop</a><a style="width:91px">Map</a><a style="width:151px">Testimonials</a><a style="width:125px">About Us</a><a style="width:99px">Blog</a><a style="width:129px">Contact Us</a>
    <a class="cart">Cart 0 itmes</a>
  </nav>

  <header class="banner abs">
    <div class="brand-dot abs"></div>
    <div class="brand-name abs">BRLV Careers</div>
    <h1 class="abs">CV Writing for IT Professionals</h1>
  </header>

  <article class="product abs" style="left:201px">
    <div class="product-head">Thinking &nbsp;you career needs a new CV, Cover Letter &amp; Linkfolio profile?</div>
    <div class="product-photo abs"><div role="img" aria-label="Close-up of a printed curriculum vitae" style="background:linear-gradient(160deg,#3d6f96,#c9dbe8 45%,#eef3f7)"></div></div>
    <div class="price abs">Worth: $700<br>Only $395</div>
    <div class="btn-click abs">CLICK HERE</div>
    <div class="stars abs">★★★<span>★★</span></div>
    <div class="reviews abs">Tetimonials<br>7 Customer Reviews</div>
    <ul class="features abs">
      <li><svg width="14" height="13"><path d="M1 7l4 4 8-10" stroke="#bbb" stroke-width="2" fill="none"/></svg>One Week Turnaround</li>
      <li><svg width="14" height="13"><path d="M1 7l4 4 8-10" stroke="#bbb" stroke-width="2" fill="none"/></svg>Dedicated CV Writer</li>
      <li><svg width="14" height="13"><path d="M1 7l4 4 8-10" stroke="#bbb" stroke-width="2" fill="none"/></svg>New CV in DocWrite</li>
      <li><svg width="14" height="13"><path d="M1 7l4 4 8-10" stroke="#bbb" stroke-width="2" fill="none"/></svg>Optimised Linkfolio Profile</li>
      <li><svg width="14" height="13"><path d="M1 7l4 4 8-10" stroke="#bbb" stroke-width="2" fill="none"/></svg>Money-back Guarantee</li>
    </ul>
  </article>

  <article class="product abs" style="left:546px">
    <div class="product-head">Thinking &nbsp;you career needs a new CV, Cover Letter &amp; Linkfolio profile?</div>
    <div class="product-photo abs"><div role="img" aria-label="Businessman leaping forward" style="background:linear-gradient(#b9b9b9,#7d7d7d)"></div></div>
    <div class="price abs">Worth: $700<br>Only $395</div>
    <div class="btn-click abs">CLICK HERE</div>
    <div class="stars abs">★★★<span>★★</span></div>
    <div class="reviews abs">Tetimonials<br>7 Customer Reviews</div>
    <ul class="features abs">
      <li><svg width="14" height="13"><path d="M1 7l4 4 8-10" stroke="#bbb" stroke-width="2" fill="none"/></svg>One Week Turnaround</li>
      <li><svg width="14" height="13"><path d="M1 7l4 4 8-10" stroke="#bbb" stroke-width="2" fill="none"/></svg>Dedicated CV Writer</li>
      <li><svg width="14" height="13"><path d="M1 7l4 4 8-10" stroke="#bbb" stroke-width="2" fill="none"/></svg>New CV in DocWrite</li>
      <li><svg width="14" height="13"><path d="M1 7l4 4 8-10" stroke="#bbb" stroke-width="2" fill="none"/></svg>Optimised Linkfolio Profile</li>
      <li><svg width="14" height="13"><path d="M1 7l4 4 8-10" stroke="#bbb" stroke-width="2" fill="none"/></svg>Money-back Guarantee</li>
    </ul>
  </article>

  <aside class="side-card abs">
    <div class="side-row abs" style="top:0;height:85px">
      <div class="abs" style="left:14px;top:30px;font-size:13px;font-weight:600;color:var(--navy)">BRLV</div>
      <div class="abs" style="left:62px;top:30px;font-size:13px;color:#222;white-space:nowrap">IT Specialist CV &amp; Linkfolio Profiles</div>
    </div>
    <div class="side-row abs" style="top:85px;height:156px">
      <div class="seal abs" role="img" aria-label="30 day money-back guarantee seal" style="left:14px;top:16px;width:106px;height:106px"></div>
      <div class="track abs" style="top:12px">Poven track record:<br><span class="dim">300 IT Palecements</span><br>100% Client Statisfaction<br><span class="dim">20,000 IT CV's Reviewed</span><br>7 Years in IT Recruitment</div>
    </div>
    <div class="side-row abs" style="top:241px;height:57px"></div>
    <div class="partner abs" role="img" aria-label="University partner badge" style="left:25px;width:70px"></div>
    <div class="partner abs" role="img" aria-label="Project management certification badge" style="left:126px;width:80px"></div>
    <div class="partner abs" role="img" aria-label="Professional network badge" style="left:231px;width:34px"></div>
    <div class="contact-photo abs" role="img" aria-label="Portrait of consultant Marcus"></div>
    <div class="contact-text abs">Contact Marcus anytime on<br>+613 9000 4821</div>
  </aside>

  <div class="social linkfolio abs">Connect with me on Linkfolio<span class="ico"></span></div>
  <div class="social circlepost abs">Follow me on Circlepost<span class="ico"></span></div>

  <section class="testi-card abs">
    <div class="testi-head">Testimonials</div>
    <div class="testi-photo abs" role="img" aria-label="Portrait of a client in a suit"></div>
    <p class="testi-text abs">Lorem ipsum dolor sit amet, consectetuer adipiscing elit. Aenean commodo ligula eget dolor. Aenean massa.</p>
  </section>

  <div class="register abs"><strong>Register Easily for Our Free</strong><span>Recuritment coaching newletters<br>and special offers</span></div>

  <div class="shop-band abs">SHOP: CV Writting, Linkfolio, Selection Criteria, Cover Letter, Recruitment &amp; Interview Coaching</div>
  <section class="how abs">
    <h2 class="abs">How We Will writer your CV and Linkfolio Profile:</h2>
    <ol class="abs">
      <li>Nascetur ridiculus mus.Donec quam felis, ultricies nec,</li>
      <li>Lorem ipsum dolor sit amet, consectetuer adipiscing elit</li>
      <li>Aenean commodo ligula eget dolor. Aenean massa. Cum</li>
      <li>Sociis natoque penatibus et magnis dis parturient montes,</li>
      <li>Nascetur ridiculus mus.Donec quam felis, ultricies nec,</li>
      <li>Pellentesque eu, pretium quis</li>
    </ol>
    <div class="seal abs" role="img" aria-label="30 day money-back guarantee seal" style="left:503px;top:66px;width:104px;height:104px"></div>
  </section>

  <h2 class="section-title abs">Testimonial</h2>
  <section class="quote abs">
    <div class="quote-photo abs" role="img" aria-label="Portrait of a smiling client"></div>
    <h3 class="abs">Nullam lacus nunc, gravida</h3>
    <p class="abs">Lorem ipsum dolor sit amet, consectetuer adipiscing elit. Aenean commodo ligula eget dolor. Aenean massa. &nbsp;Lorem ipsum dolor sit amet, consectetuer adipiscing elit. Aenean commodo ligula eget dolor. Aenean massa.</p>
  </section>

  <footer class="site-footer abs">
    <span class="copy abs">©2014 BRLV CAREERS, ALL RIGHTS RESERVED.</span>
    <nav class="abs">HOME &nbsp; &nbsp;| &nbsp; &nbsp;SHOP &nbsp; &nbsp;| TESTIMONIALS| &nbsp;CONTACT US</nav>
  </footer>

</div>
</body>
</html>
```